Animal Eye Clinic needs a Business card

We are a new veterinary ophthalmology practice (Tessaly Animal Eye Care) and we need a business card designed. We only see animal eyes - we are not a regular veterinary clinic. We already have a logo. We are looking for a professional, good looking business card to hand out to our clients. We are looking for something simple but professional and contemporary. Our logo is likely the only picture/graphic that needs to be on the card.
Updates

Contact Information for Business Card

Marisol Dunkley, BSc, DVM, MSc, DipACVO
Veterinary Ophthalmologist

Phone: 250.418.3097
Email: tessalyanimaleyecare@mailbrook.net
Website: tessalyanimaleyecare.net
Address: 1840 Pellworth Rd
Kelowna, BC, V4T 8M3

Colors

Designer to choose colors to be used in the design.

Requirements
Must have
• Our logo (attached)

```html
<!DOCTYPE html>
<html lang="en">
<head>
<meta charset="utf-8">
<title>Tessaly Animal Eye Care — Business Card</title>
<link rel="stylesheet" href="https://fonts.googleapis.com/css2?family=Lato:wght@400;700;900&display=swap">
<style>
  :root {
    --teal: #0e9aa7;
    --teal-light: #27aab5;
    --grey: #6f6f70;
    --ink: #555556;
    --paper: #ffffff;
    --backdrop: #2b2b2d;
  }
  * { box-sizing: border-box; margin: 0; padding: 0; }
  html, body {
    width: 1200px; height: 1108px; overflow: hidden;
    background: var(--backdrop);
    font-family: "Lato", Arial, sans-serif;
  }
  .sheet {
    width: 1200px; height: 1108px;
    display: flex; flex-direction: column; align-items: center; justify-content: center;
    gap: 60px;
  }
  .card {
    width: 840px; height: 480px;
    border-radius: 26px;
    overflow: hidden;
    position: relative;
  }
  /* Front */
  .card-front {
    background: var(--teal);
    display: flex; align-items: center; justify-content: center;
  }
  .brand {
    display: flex; align-items: center; gap: 22px;
    color: var(--paper);
    font-weight: 700;
  }
  .brand-dot {
    width: 64px; height: 64px; border-radius: 50%;
    background: var(--paper);
    flex: none;
  }
  .brand-name { display: flex; flex-direction: column; line-height: 1; }
  .brand-top { font-size: 22px; letter-spacing: 19px; text-transform: uppercase; margin-bottom: 8px; }
  .brand-main { font-size: 44px; text-transform: uppercase; letter-spacing: 1px; }

  /* Back */
  .card-back { background: var(--paper); }
  .artwork {
    position: absolute; left: 0; top: 0;
    width: 840px; height: 480px;
  }
  .details {
    position: absolute; right: 48px; top: 56px;
    display: flex; flex-direction: column; align-items: flex-end;
    text-align: right;
  }
  .details .brand { color: var(--teal); }
  .details .brand-top { font-size: 17px; letter-spacing: 15px; margin-bottom: 6px; margin-right: -15px; }
  .details .brand-main { font-size: 32px; }
  .person { margin-top: 48px; display: flex; flex-direction: column; align-items: flex-end; }
  .person-name { color: var(--teal); font-weight: 900; font-size: 23px; letter-spacing: 1px; text-transform: uppercase; }
  .person-creds { color: var(--teal); font-weight: 900; font-size: 16px; letter-spacing: .5px; margin-top: 2px; }
  .person-role { color: var(--ink); font-size: 17px; margin-top: 2px; }
  .contact { margin-top: 18px; color: var(--ink); font-size: 18px; line-height: 1.45; list-style: none; }
</style>
</head>
<body>
<main class="sheet">
  <section class="card card-front" aria-label="Card front">
    <div class="brand">
      <span class="brand-dot"></span>
      <span class="brand-name">
        <span class="brand-top">Tessaly</span>
        <span class="brand-main">Animal Eye Care</span>
      </span>
    </div>
  </section>

  <section class="card card-back" aria-label="Card back">
    <svg class="artwork" viewBox="0 0 840 480" role="img" aria-label="Teal and grey artwork of dog, cat and horse silhouettes">
      <defs>
        <linearGradient id="art-fill" x1="0" y1="0" x2="0.6" y2="1">
          <stop offset="0" stop-color="#0e9aa7"/>
          <stop offset="0.7" stop-color="#27aab5"/>
          <stop offset="1" stop-color="#6f6f70"/>
        </linearGradient>
      </defs>
      <path d="M0 0 H500 C430 60 395 130 380 220 C368 300 352 390 320 480 H0 Z" fill="url(#art-fill)"/>
    </svg>

    <div class="details">
      <div class="brand">
        <span class="brand-name">
          <span class="brand-top">Tessaly</span>
          <span class="brand-main">Animal Eye Care</span>
        </span>
      </div>
      <div class="person">
        <p class="person-name">Marisol Dunkley</p>
        <p class="person-creds">BSc, DVM, MSc, DipACVO</p>
        <p class="person-role">Veterinary Ophthalmologist</p>
      </div>
      <ul class="contact">
        <li>Phone : 250.418.3097</li>
        <li>tessalyanimaleyecare@mailbrook.net</li>
        <li>www.tessalyanimaleyecare.net</li>
        <li>1840 Pellworth Rd, Kelowna, BC, V4T 8M3</li>
      </ul>
    </div>
  </section>
</main>
</body>
</html>
```